Improving the design of the attached webpage jpg image

Make the page professional, but keep it simple. All elements on the page can be changed to anything you like EXCEPT the blue bar at the top of the page.

The two images are the same page.

The content on the page must all be there. Do not add new content.

The design needs to feel like a professional score report.
Updates

Need extra days to review

Industry/Entity Type

Education

Number of Pages Required

1 page

Colors

Designer to choose colors to be used in the design.

Requirements
Must have
• The blue bar color and the bars themselves at the top and bottom of the page. All the content on the page.

```html
<!DOCTYPE html>
<html lang="en">
<head>
<meta charset="utf-8">
<title>TopScore Prep GBAT Score Report</title>
<link href="https://fonts.googleapis.com/css2?family=Montserrat:wght@400;500;600;700&display=swap" rel="stylesheet">
<style>
:root{
  --brand:#3e778c;
  --brand-soft:#eaf2f5;
  --ink:#263238;
  --text:#4a5a61;
  --muted:#8c979c;
  --line:#e4e8ea;
  --surface:#f7f9fa;
  --track:#e3e6e8;
  --red:#e23d22;
  --orange:#e8861c;
  --green:#4fb04a;
}
*{box-sizing:border-box;margin:0;padding:0}
html,body{width:1200px;height:1188px;overflow:hidden;background:#fff;font-family:"Montserrat",sans-serif;color:var(--text)}
.top-bar{position:absolute;left:0;top:0;width:1200px;height:48px;background:var(--brand)}

.report-header{position:absolute;left:124px;top:80px;width:952px}
.report-title{font-size:24px;font-weight:700;color:var(--ink);letter-spacing:-.2px}
.meta{display:flex;gap:24px;margin-top:12px;font-size:13px;font-weight:500;color:var(--text)}
.meta .item{display:flex;align-items:center;gap:8px}

.summary-card{position:absolute;left:124px;top:164px;width:952px;height:152px;border:1px solid var(--line);border-radius:10px;background:var(--surface);display:flex;align-items:center}
.score-block{width:172px;height:100%;display:flex;flex-direction:column;align-items:center;justify-content:center;border-right:1px solid var(--line)}
.score-gauge{position:relative;width:96px;height:96px}
.score-gauge .value{position:absolute;inset:0;display:flex;align-items:center;justify-content:center;font-size:26px;font-weight:700;color:var(--red)}
.score-total{margin-top:8px;font-size:12px;font-weight:600;color:var(--muted);letter-spacing:.3px}
.summary{flex:1;padding:0 32px;font-size:13px;line-height:22px;color:var(--text)}

.tabs{position:absolute;left:124px;top:344px;width:952px;height:40px;border-bottom:1px solid var(--line);display:flex;gap:32px}
.tab{position:relative;font-size:14px;font-weight:500;color:var(--muted);line-height:28px;white-space:nowrap}
.tab.active{color:var(--brand);font-weight:600}
.tab.active::after{content:"";position:absolute;left:0;right:0;top:37px;height:3px;border-radius:2px;background:var(--brand)}

.section-title{position:absolute;left:124px;font-size:18px;font-weight:600;color:var(--ink)}

.perf-table{position:absolute;left:124px;top:448px;width:952px;height:266px;border:1px solid var(--line);border-radius:10px;overflow:hidden}
.perf-head{position:relative;height:40px;background:var(--surface);border-bottom:1px solid var(--line);font-size:12px;font-weight:600;color:var(--muted);text-transform:uppercase;letter-spacing:.6px}
.perf-head span{position:absolute;top:13px}
.perf-row{position:absolute;left:0;width:100%;height:56px;border-bottom:1px solid var(--line)}
.perf-row:last-child{border-bottom:none}
.perf-row .name{position:absolute;left:24px;top:19px;font-size:14px;font-weight:600;color:var(--ink)}
.perf-row .pct{position:absolute;left:300px;top:15px;width:56px;height:26px;border-radius:13px;background:var(--brand-soft);font-size:13px;font-weight:600;line-height:26px;text-align:center;color:var(--brand)}
.scale{position:absolute;left:444px;top:0;width:476px;height:56px}
.scale .lbl{position:absolute;top:8px;font-size:11px;font-weight:500;color:var(--muted)}
.scale .lbl.mid{transform:translateX(-50%)}
.scale .track{position:absolute;left:0;right:0;top:32px;height:6px;border-radius:3px;background:var(--track)}
.scale .fill{position:absolute;left:0;top:0;height:6px;border-radius:3px}
.scale .tick{position:absolute;top:27px;width:2px;height:16px;margin-left:-1px;border-radius:1px;background:#b9c2c6}
.scale .badge{position:absolute;top:25px;height:20px;width:38px;margin-left:-19px;border-radius:10px;color:#fff;font-size:11px;font-weight:700;line-height:20px;text-align:center;box-shadow:0 0 0 2px #fff}

.chart-box{position:absolute;left:124px;top:780px;width:952px;height:260px;border:1px solid var(--line);border-radius:10px}
.chart-box svg{display:block}
.axis{font-family:"Montserrat",sans-serif;font-size:11px;font-weight:500;fill:var(--muted)}
</style>
</head>
<body>
<div class="top-bar"></div>

<header class="report-header">
  <h1 class="report-title">TopScore Prep GBAT Score Report</h1>
  <div class="meta">
    <span class="item">
      <svg width="15" height="15" viewBox="0 0 15 15" aria-hidden="true" fill="none" stroke="#3e778c" stroke-width="1.2">
        <rect x="1.5" y="2.5" width="12" height="11" rx="1.5"/><line x1="1.5" y1="5.5" x2="13.5" y2="5.5"/>
        <line x1="4.5" y1="1" x2="4.5" y2="4"/><line x1="10.5" y1="1" x2="10.5" y2="4"/>
      </svg>
      September 4, 2024
    </span>
    <span class="item">
      <svg width="14" height="15" viewBox="0 0 14 15" aria-hidden="true" fill="none" stroke="#3e778c" stroke-width="1.2">
        <path d="M2.5 1.5h6l3.5 3.5v8.5h-9.5z"/><path d="M8.5 1.5v3.5h3.5"/>
        <line x1="5" y1="8.5" x2="9.5" y2="8.5"/><line x1="5" y1="10.5" x2="9.5" y2="10.5"/>
      </svg>
      Simulation test 2
    </span>
  </div>
</header>

<section class="summary-card">
  <div class="score-block">
    <div class="score-gauge">
      <svg width="96" height="96" viewBox="0 0 96 96" aria-hidden="true">
        <circle cx="48" cy="48" r="42" fill="none" stroke="#e3e6e8" stroke-width="6"/>
        <circle cx="48" cy="48" r="42" fill="none" stroke="#e23d22" stroke-width="6" stroke-linecap="round" stroke-dasharray="31 233" transform="rotate(-90 48 48)"/>
      </svg>
      <div class="value">275</div>
    </div>
    <div class="score-total">275/805</div>
  </div>
  <p class="summary">From classic novels like "Hearts and Hollows" by Eleanor Whitcombe to contemporary bestsellers like "Milo Thornwick" by R.A. Penhallow, literature transcends time and culture, touching the hearts and minds of readers. The power of storytelling allows us to escape reality, gain empathy, and explore diverse perspectives, making literature an indispensable part of the human experience.</p>
</section>

<nav class="tabs">
  <span class="tab active">Overall performance</span>
  <span class="tab">Quantitative reasoning</span>
  <span class="tab">Verbal reasoning</span>
  <span class="tab">Data insights</span>
</nav>

<h2 class="section-title" style="top:414px">Section performance</h2>

<div class="perf-table">
  <div class="perf-head">
    <span style="left:24px">Section</span>
    <span style="left:300px">Percentile</span>
    <span style="left:444px">Score</span>
  </div>

  <div class="perf-row" style="top:41px">
    <span class="name">Overall performance</span>
    <span class="pct">1st</span>
    <div class="scale">
      <span class="lbl" style="left:0">205</span>
      <span class="lbl mid" style="left:56.8%">546</span>
      <span class="lbl" style="right:0">805</span>
      <div class="track"><div class="fill" style="width:11.7%;background:var(--red)"></div></div>
      <div class="tick" style="left:56.8%"></div>
      <div class="badge" style="left:11.7%;background:var(--red)">275</div>
    </div>
  </div>

  <div class="perf-row" style="top:97px">
    <span class="name">Quantitative reasoning</span>
    <span class="pct">2nd</span>
    <div class="scale">
      <span class="lbl" style="left:0">60</span>
      <span class="lbl mid" style="left:60%">78</span>
      <span class="lbl" style="right:0">90</span>
      <div class="track"><div class="fill" style="width:10%;background:var(--red)"></div></div>
      <div class="tick" style="left:60%"></div>
      <div class="badge" style="left:10%;background:var(--red)">63</div>
    </div>
  </div>

  <div class="perf-row" style="top:153px">
    <span class="name">Verbal reasoning</span>
    <span class="pct">1st</span>
    <div class="scale">
      <span class="lbl" style="left:0">60</span>
      <span class="lbl mid" style="left:50%">75</span>
      <span class="lbl" style="right:0">90</span>
      <div class="track"><div class="fill" style="width:16.7%;background:var(--orange)"></div></div>
      <div class="tick" style="left:50%"></div>
      <div class="badge" style="left:16.7%;background:var(--orange)">65</div>
    </div>
  </div>

  <div class="perf-row" style="top:209px">
    <span class="name">Data insights</span>
    <span class="pct">5th</span>
    <div class="scale">
      <span class="lbl" style="left:0">60</span>
      <span class="lbl mid" style="left:43.3%">73</span>
      <span class="lbl" style="right:0">90</span>
      <div class="track"><div class="fill" style="width:66.7%;background:var(--green)"></div></div>
      <div class="tick" style="left:43.3%"></div>
      <div class="badge" style="left:66.7%;background:var(--green)">80</div>
    </div>
  </div>
</div>

<h2 class="section-title" style="top:746px">Score distribution</h2>

<div class="chart-box">
  <svg width="950" height="258" viewBox="0 0 950 258" role="img" aria-label="Bar chart of score distribution across five sections">
    <g stroke="#edf0f1" stroke-width="1">
      <line x1="80" y1="30" x2="910" y2="30"/>
      <line x1="80" y1="75" x2="910" y2="75"/>
      <line x1="80" y1="120" x2="910" y2="120"/>
      <line x1="80" y1="165" x2="910" y2="165"/>
    </g>
    <line x1="80" y1="210" x2="910" y2="210" stroke="#cfd6d9" stroke-width="1"/>
    <g class="axis" text-anchor="end">
      <text x="62" y="34">100%</text>
      <text x="62" y="79">80%</text>
      <text x="62" y="124">50%</text>
      <text x="62" y="169">25%</text>
      <text x="62" y="214">0</text>
    </g>
    <g fill="#3e778c">
      <path d="M141 210V56q0-4 4-4h36q4 0 4 4V210z"/>
      <path d="M307 210V92q0-4 4-4h36q4 0 4 4V210z"/>
      <path d="M473 210V146q0-4 4-4h36q4 0 4 4V210z"/>
      <path d="M639 210V34q0-4 4-4h36q4 0 4 4V210z"/>
      <path d="M805 210V34q0-4 4-4h36q4 0 4 4V210z"/>
    </g>
    <g class="axis" text-anchor="middle">
      <text x="163" y="234">1</text>
      <text x="329" y="234">2</text>
      <text x="495" y="234">3</text>
      <text x="661" y="234">4</text>
      <text x="827" y="234">5</text>
    </g>
  </svg>
</div>
</body>
</html>
```